Modern and Sleek Non-Fiction Book Cover Design

Seeking a talented graphic designer to create a modern and sleek cover and back page for a book to be published on Pagewick . The design should be visually appealing and align with the book's theme, using bright colors to make it stand out. The title is "The Counsel Office Welcome Manual" with "The" in a smaller font, and the tagline "Intake as a Competitive Advantage" should be included. The book is targeted at an audience interested in immigration and family law firms. So I would like it on the cover as well. The hex numbers for the colors are 00aeeef, fcb034, and 336a89. The cover should feature the author's photo prominently.
-Design a modern front cover for the book
-Design a sleek back page for the book
-Ensure designs meet Pagewick publishing requirements 8x5 paperback
Let's not use the side image, it doesn't seem to fit like I thought it might.

```html
<!DOCTYPE html>
<html lang="en">
<head>
<meta charset="UTF-8">
<title>The Counsel Office Welcome Manual — Cover</title>
<link rel="stylesheet" href="https://fonts.googleapis.com/css2?family=Tinos&family=Dancing+Script:wght@500&display=swap">
<style>
  :root {
    --teal-deep: #0d6f86;
    --teal-mid: #6aa6b0;
    --mist: #eef0ec;
    --cream: #f5f5ea;
    --ink-teal: #3a8096;
    --gold-light: #e8d9a6;
    --gold: #c9b06d;
    --gold-dark: #a48d52;
    --rule-white: #f4f3ec;
  }
  * { margin: 0; padding: 0; box-sizing: border-box; }
  html, body {
    width: 1200px;
    height: 900px;
    overflow: hidden;
    background: var(--mist);
  }
  .cover {
    position: relative;
    width: 1200px;
    height: 900px;
    overflow: hidden;
  }
  .side-panel {
    position: absolute;
    top: 0;
    width: 334px;
    height: 900px;
    background: linear-gradient(to bottom, var(--mist) 0%, #c4d6d6 25%, var(--teal-mid) 50%, #3f8d9f 72%, var(--teal-deep) 100%);
  }
  .side-panel--left { left: 0; }
  .side-panel--right { left: 866px; }
  .rule {
    position: absolute;
    width: 334px;
    height: 4px;
  }
  .rule--gold {
    background: linear-gradient(to right, var(--gold-dark), var(--gold-light) 50%, var(--gold));
  }
  .rule--white { background: var(--rule-white); height: 5px; }
  .rule--left-gold { left: 0; top: 429px; }
  .rule--left-white { left: 0; top: 527px; }
  .rule--right-white { left: 866px; top: 362px; }
  .rule--right-gold { left: 866px; top: 464px; }
  .center-panel {
    position: absolute;
    left: 334px;
    top: 0;
    width: 532px;
    height: 900px;
    background: var(--cream);
  }
  .emblem-area {
    position: absolute;
    left: 88px;
    top: 144px;
    width: 356px;
    height: 254px;
    background: linear-gradient(160deg, var(--gold-light) 0%, var(--gold) 50%, var(--gold-dark) 100%);
    opacity: 0.85;
  }
  .book-title {
    position: absolute;
    left: 100px;
    top: 462px;
    font-family: "Tinos", "Times New Roman", serif;
    font-weight: 400;
    font-size: 58px;
    line-height: 78px;
    color: var(--ink-teal);
    letter-spacing: 0.5px;
  }
  .book-title span { display: block; white-space: nowrap; }
  .tagline {
    position: absolute;
    left: 100px;
    top: 824px;
    font-family: "Dancing Script", cursive;
    font-weight: 500;
    font-size: 21px;
    color: var(--ink-teal);
    white-space: nowrap;
  }
</style>
</head>
<body>
  <main class="cover">
    <div class="side-panel side-panel--left"></div>
    <div class="side-panel side-panel--right"></div>
    <div class="rule rule--gold rule--left-gold"></div>
    <div class="rule rule--white rule--left-white"></div>
    <div class="rule rule--white rule--right-white"></div>
    <div class="rule rule--gold rule--right-gold"></div>

    <section class="center-panel">
      <div class="emblem-area" role="img" aria-label="Gold geometric emblem with fine line work"></div>
      <h1 class="book-title">
        <span>The</span>
        <span>Counsel Office</span>
        <span>Welcome</span>
        <span>Manual</span>
      </h1>
      <p class="tagline">Intake as a Competitive Advantage</p>
    </section>
  </main>
</body>
</html>
```